Need Primer (paint) Label Design

THE ATTACHED LABEL/S ARE SOLEY FOR REFERENCE. DO NOT MAKE ME AN INTERIOR PAINT OR CHALK PAINT LABEL. I ONLY NEED A "PRIMER" LABEL. THE ATTACHED INTERIOR PAINT LABEL IS ONLY TO SHOW YOU THE THEME/DESIGN OF OUR OTHER LABELS. THE BLUE LABEL ONLY HAS A DESIGN ASPECT I LIKE (PRIMER ON SIDE). The last four labels are our competitors.
```````````````````````````````````````````````````````````````````````````````````````````````````
We need this label to look professional, sharp, eye catching and modern.
OUR PRIMARY COLORS ARE BLACK AND WHITE. IF YOU INCOPORATE ANOTHER COLOR, SILVER OR GOLD MIGHT BE IDEAL BUT PLEASE DON'T DRIFT TOO FAR.
The attached documents:
1st - Our Logo
2nd - Our chalk paint label (reference). We do not need a chalk paint label.
3rd. A random design example. I like the PRIME on the side running vertically. I think it's a cool design concept.
````````````````````````````````````````````````````````````````````````````````````````````````````
We are going to be using a normal paint can with a metal bail/handle so please use that with you design work
``````````````````````````````````````````````````````````````````````````````````````````````````
Order, in my head:
4327
Coatings
^^ I want this to stand out as well but I don't want it to be the first thing your eye is drawn to. Probably 2nd
Interior/Exterior
Multi - Surface Primer
^^ Want this to stick out and draw your eye so the customer knows what it is immediately
Exceptional Adhesion, Performance, Durability,
Use on Wood, Drywall, Plaster, Stucco, Masonry, Brick, Paneling, Painted Metal, & Properly Prepared Glossy Surfaces & More
35* Lowe Temperature Application (can be on side or small)
100% Acrylic
Low Odor - Low VOC - Soap & Water Clean Up
1 US Gallon - 3.785 L
Feel free to get creative with it!

```html
<!DOCTYPE html>
<html lang="en">
<head>
<meta charset="utf-8">
<title>4327 Coatings – Multi-Surface Primer Label</title>
<link href="https://fonts.googleapis.com/css2?family=Poppins:wght@500;600;700&family=Kumbh+Sans:wght@500;600&family=Questrial&display=swap" rel="stylesheet">
<style>
  :root {
    --ink: #0a0a0a;
    --paper: #ffffff;
    --edge: #e2e2e2;
    --shadow: rgba(0,0,0,0.45);
    --silver-light: #ffffff;
    --silver-dark: #8c8c8c;
  }
  html, body {
    margin: 0;
    padding: 0;
    width: 1200px;
    height: 983px;
    overflow: hidden;
    background: var(--paper);
  }
  .canvas {
    position: relative;
    width: 1200px;
    height: 983px;
    color: var(--ink);
    font-family: "Kumbh Sans", sans-serif;
  }
  .label {
    position: absolute;
    left: 154px;
    top: 125px;
    width: 933px;
    height: 719px;
    background: var(--paper);
    border-top: 1px solid var(--edge);
    box-shadow: 4px 4px 4px var(--shadow);
  }
  .silver-panel {
    position: absolute;
    left: 796px;
    top: 546px;
    width: 275px;
    height: 261px;
    background: linear-gradient(90deg, var(--silver-light) 0%, #d6d6d6 40%, var(--silver-dark) 100%);
  }
  .brand {
    position: absolute;
    left: 500px;
    top: 196px;
    width: 211px;
    text-align: center;
    font-family: "Poppins", sans-serif;
    font-weight: 500;
  }
  .brand-number {
    display: block;
    font-size: 112px;
    line-height: 1;
    letter-spacing: -2px;
  }
  .brand-word {
    display: block;
    margin-top: 2px;
    font-size: 28px;
    letter-spacing: 11px;
    padding-left: 11px;
    line-height: 1;
  }
  .use-type {
    position: absolute;
    left: 460px;
    top: 384px;
    width: 300px;
    text-align: center;
    font-family: "Questrial", sans-serif;
    font-size: 51px;
    line-height: 57px;
  }
  .divider {
    position: absolute;
    top: 567px;
    width: 2px;
    height: 203px;
    background: var(--ink);
  }
  .divider--left { left: 471px; }
  .divider--right { left: 749px; }
  .feature {
    position: absolute;
    text-align: center;
    font-family: "Poppins", sans-serif;
    font-weight: 600;
    font-size: 11px;
    line-height: 14px;
    width: 110px;
  }
  .feature svg { display: block; margin: 0 auto 4px; }
  .feature--odor { left: 189px; top: 588px; }
  .feature--voc { left: 353px; top: 592px; }
  .feature--cleanup { left: 187px; top: 688px; }
  .feature--temp { left: 346px; top: 696px; }
  .temp-mark {
    display: flex;
    align-items: center;
    justify-content: center;
    gap: 4px;
    font-size: 24px;
    font-weight: 700;
    line-height: 26px;
    margin-bottom: 5px;
  }
  .temp-mark svg { margin: 0; }
  .benefits {
    position: absolute;
    left: 480px;
    top: 605px;
    width: 260px;
    text-align: center;
    font-family: "Kumbh Sans", sans-serif;
    font-weight: 500;
    font-size: 22px;
    line-height: 28px;
  }
  .acrylic {
    position: absolute;
    left: 480px;
    top: 713px;
    width: 260px;
    text-align: center;
    font-family: "Questrial", sans-serif;
    font-size: 25px;
    line-height: 26px;
  }
  .surfaces {
    position: absolute;
    left: 764px;
    top: 598px;
    width: 220px;
    text-align: center;
    font-family: "Kumbh Sans", sans-serif;
    font-weight: 500;
    font-size: 10.5px;
    line-height: 24.6px;
  }
  .volume {
    position: absolute;
    left: 774px;
    top: 720px;
    width: 200px;
    text-align: center;
    font-family: "Questrial", sans-serif;
    font-size: 20px;
    line-height: 21px;
  }
  .product-title {
    position: absolute;
    left: 0;
    top: 0;
    width: 1200px;
    height: 983px;
    pointer-events: none;
  }
  .product-title text { fill: var(--ink); font-family: "Poppins", sans-serif; }
  .title-multi { font-weight: 700; font-size: 120px; }
  .title-surface { font-weight: 600; font-size: 60px; }
</style>
</head>
<body>
<main class="canvas">
  <section class="label">
  </section>
  <div class="silver-panel"></div>

  <header class="brand">
    <span class="brand-number">4327</span>
    <span class="brand-word">COATINGS</span>
  </header>

  <h2 class="use-type" style="margin:0;font-weight:400;">INTERIOR<br>EXTERIOR</h2>

  <div class="feature feature--odor">
    <svg width="40" height="48" viewBox="0 0 40 48" fill="none" stroke="#0a0a0a" stroke-width="1.6" stroke-linecap="round">
      <path d="M14 2 C16 14 32 22 30 32 C28 40 18 38 14 34 C10 40 2 38 4 32 C6 28 10 30 12 31"/>
      <path d="M14 24 L21 30 M21 24 L14 30"/>
    </svg>
    Low Odor
  </div>

  <div class="feature feature--voc">
    <svg width="52" height="46" viewBox="0 0 52 46" fill="#0a0a0a" stroke="none">
      <path d="M14 4 C8 12 18 18 12 28 C9 34 12 40 14 44 L18 44 C15 38 14 33 18 27 C23 18 12 12 17 4 Z"/>
      <path d="M26 2 C20 10 30 17 24 27 C21 33 24 39 26 44 L30 44 C27 38 26 32 30 26 C35 17 24 10 29 2 Z"/>
      <path d="M38 6 C33 13 41 19 36 28 C33 34 36 40 38 44 L42 44 C39 38 38 33 42 27 C46 19 37 13 41 6 Z"/>
      <path d="M2 4 L50 40" stroke="#0a0a0a" stroke-width="2.4"/>
    </svg>
    Low VOC
  </div>

  <div class="feature feature--cleanup">
    <svg width="24" height="42" viewBox="0 0 24 42" fill="none" stroke="#0a0a0a" stroke-width="1.8">
      <circle cx="9" cy="5" r="3.5"/>
      <circle cx="6" cy="14" r="4"/>
      <circle cx="16" cy="11" r="4"/>
      <path d="M13 20 C11 28 6 31 7 35 C8 40 18 40 19 35 C20 31 15 28 13 20 Z"/>
    </svg>
    Soap &amp; Water<br>Clean Up
  </div>

  <div class="feature feature--temp">
    <div class="temp-mark">
      <svg width="32" height="32" viewBox="0 0 32 32" fill="#0a0a0a">
        <path d="M20 2 L30 12 L24 18 L14 8 Z"/>
        <path d="M14 10 L22 18 L18 20 L12 14 Z"/>
        <path d="M13 15 L17 19 L5 31 C3 32 1 30 2 28 Z"/>
      </svg>
      <span>35*</span>
    </div>
    Lowe Temperature<br>Application
  </div>

  <div class="divider divider--left"></div>
  <div class="divider divider--right"></div>

  <p class="benefits" style="margin:0;">Exceptional Adhesion<br>Performance<br>Durability</p>
  <p class="acrylic" style="margin:0;">100%<br>ACRYLIC</p>

  <p class="surfaces" style="margin:0;">Use on Wood, Drywall, Plaster,<br>Stucco, Masonry, Brick, Paneling,<br>Painted Metal, &amp; Properly Prepared<br>Glossy Surfaces &amp; More</p>
  <p class="volume" style="margin:0;">1 US GALLON<br>3.785 L</p>

  <svg class="product-title" viewBox="0 0 1200 983" aria-label="Multi-Surface Primer">
    <text class="title-multi" transform="translate(982 533) rotate(-90)" textLength="369" lengthAdjust="spacingAndGlyphs">MULTI</text>
    <text class="title-surface" transform="translate(1038 770) rotate(-90)" textLength="608" lengthAdjust="spacingAndGlyphs">SURFACE PRIMER</text>
  </svg>
</main>
</body>
</html>
```